Kelro DIGITAL HORIZON learning portal

We beed a flyer design to launch our new DIGITAL HORIZON Learning Portal. The flyer will be used in letter box drops and to give to small business to encourage sales of this new service.

ABOUT US:

We are a small training firm offering world class training solutions in the areas of:

1. Time Management
2. Sales skills
3. Strategic & High performance leadership
4. Sales Management
5. Personal Maximum Achievement.

You can find our website at www.kelro-example.com.au

ABOUT DIGITAL HORIZON Learning Portal:

We are launching an online learning portal called DIGITAL HORIZON Learning Portal which will allow anyone, anywhere in the world to take our courses online as long as they have access to a PC, smart phone and internet.

Taking an online course with Kelro through our DIGITAL HORIZON Learning Portal will allow students/participants to save over 50% of the normal price of attending a face to face training program.

There are over 80 different individual learning units that can be taken by a student/participant. The participant can choose to take any unit they wish building their own unique learning experience or they can take a full course in one of the subject areas listed above in the about us section.

ADVANTAGES OF USING THE Kelro DIGITAL HORIZON Learning Portal:

* Cost effective, save over 50% by learning online compared to attending a Kelro class room based programme.
* learning can be scheduled around work and family
* Reduces travel time and travel costs
* Students/participants have the option to select learning materials that meets their level of knowledge and interest.
* Complete flexibility to build a personalised learning experience.
* Students/participants can study anywhere they have access to a computer and Internet connection
* Self-paced learning modules allow students/participants to work at their own pace
* Develops knowledge of the Internet and computers skills that will help learners throughout their lives and careers
* Successfully completing online or computer-based courses builds self-knowledge and self-confidence and encourages students to take responsibility for their learning
* Join over 4 million people who have successfully undertaken the training world wide at a time & a place convenient to students/participants.
* pay securely using swiftcoin
* learn based on a students/participants personal financial circumstances with individual units priced at $82.50 each (this is Australian dollars & includes GST)

The final design will be one that conveys flexibility of learning, cost effectiveness of the online learning solution. The flyer design can either be folded, single or double sided, A4 or A5 or DL size - whatever works best in the final outcome.

Industry/Entity Type

Small Business

Requirements
Must have
• The flyer must include:

* the "DIGITAL HORIZON Learning portal" logo and the "Kelro logo" and use the Kelro font. Several logos have been provided and the most appropriate ones can be chosen for the design. The font has been provided. (I do have other logo files in different file formats if required to aid designers)

* The flyer must direct people to the Kelro website www.kelro-example.com.au to pay, enrol and find out other information about the courses.

* The flyer must highlight cost effectiveness of the solution, the world wide popularity of the programs (over 4 million people have completed the programs world wide), flexibility of learning & the diversity of study areas.

Because of price changes in future of courses it would be very beneficial to be able to edit files in future to show new prices if and when that happens.

```html
<!DOCTYPE html>
<html lang="en">
<head>
<meta charset="utf-8">
<title>Kelro DIGITAL HORIZON flyer</title>
<link href="https://fonts.googleapis.com/css2?family=Open+Sans:wght@400;600;700&family=Parisienne&display=swap" rel="stylesheet">
<style>
  :root {
    --stage: #9a9a9a;
    --blue: #0f6b96;
    --blue-dark: #0b5578;
    --blue-soft: #3a8fb7;
    --blue-cell: #4aa3cf;
    --yellow: #ffc20e;
    --white: #ffffff;
    --ink: #1d1d1d;
  }
  * { margin: 0; padding: 0; box-sizing: border-box; }
  html, body { width: 1200px; height: 879px; overflow: hidden; }
  body { background: var(--stage); font-family: "Open Sans", Arial, sans-serif; position: relative; }
  .side-label { position: absolute; top: 14px; width: 200px; text-align: center; color: var(--white); font-weight: 700; font-size: 33px; letter-spacing: .5px; }
  .side-label.front { left: 183px; }
  .side-label.back { left: 803px; }
  .page { position: absolute; top: 75px; width: 617px; height: 875px; transform: scale(.8723); transform-origin: 0 0; background: var(--white); overflow: hidden; }
  .page.front { left: 31px; }
  .page.back { left: 626px; }
  .page > svg { position: absolute; inset: 0; }
  .abs { position: absolute; }
  .script { font-family: "Parisienne", cursive; color: var(--yellow); }

  /* front */
  .front-title { left: 222px; top: 320px; font-size: 31px; font-weight: 400; }
  .course-list { left: 250px; top: 372px; list-style: none; color: var(--white); font-size: 14.5px; line-height: 20.6px; }
  .course-list li { position: relative; padding-left: 26px; }
  .course-list li::before { content: ""; position: absolute; left: 2px; top: 8px; width: 5px; height: 5px; border-radius: 50%; background: var(--yellow); }
  .cost-box { left: 411px; top: 501px; width: 182px; height: 86px; background: var(--blue-soft); text-align: center; padding-top: 4px; }
  .cost-box h3 { font-family: "Parisienne", cursive; font-weight: 400; color: var(--yellow); font-size: 20px; line-height: 24px; }
  .cost-box p { color: var(--white); font-size: 8.6px; line-height: 13px; padding: 3px 10px 0; }
  .phone-box { left: 449px; top: 592px; width: 136px; height: 38px; background: var(--blue-dark); color: var(--yellow); font-size: 13px; display: flex; align-items: center; justify-content: center; gap: 8px; }
  .brand-tile { left: 26px; top: 533px; width: 118px; height: 169px; background: linear-gradient(180deg, #1a9ad6, #0b6aa8); display: flex; align-items: flex-end; justify-content: center; padding-bottom: 22px; color: var(--white); font-size: 30px; font-weight: 400; }
  .portal-name { left: 26px; top: 744px; height: 40px; display: flex; align-items: center; gap: 8px; color: var(--ink); font-size: 19px; font-weight: 700; letter-spacing: .3px; }
  .portal-name .mark { width: 16px; height: 16px; background: var(--yellow); }
  .site-box { left: 26px; top: 825px; width: 240px; height: 24px; background: var(--yellow); color: var(--white); font-size: 11.5px; line-height: 24px; padding-left: 10px; white-space: nowrap; }
  .contact-box { left: 272px; top: 825px; width: 288px; height: 24px; border: 1px solid var(--blue-soft); color: var(--blue); font-size: 7.8px; line-height: 22px; text-align: center; background: var(--white); white-space: nowrap; }

  /* back */
  .back-title { left: 30px; top: 266px; font-size: 24px; color: var(--white); white-space: nowrap; font-weight: 400; }
  .back-title .accent { color: var(--yellow); }
  .advantages { list-style: none; color: var(--white); font-size: 11.4px; line-height: 15px; }
  .advantages li { position: absolute; padding-left: 18px; }
  .advantages li::before { content: "*"; position: absolute; left: 0; top: 0; }
  .back-brand { left: 25px; top: 662px; width: 48px; height: 67px; background: linear-gradient(180deg, #1a9ad6, #0b6aa8); color: var(--white); font-size: 12px; display: flex; align-items: flex-end; justify-content: center; padding-bottom: 8px; }
  .contact-table { left: 25px; top: 747px; width: 144px; list-style: none; }
  .contact-table li { height: 17.5px; margin-bottom: .3px; display: flex; }
  .contact-table .val { flex: 1; background: var(--blue-cell); color: var(--white); font-size: 8px; line-height: 17.5px; text-align: right; padding-right: 4px; white-space: nowrap; }
  .contact-table .ico { width: 16px; background: var(--yellow); display: flex; align-items: center; justify-content: center; }
</style>
</head>
<body>
  <div class="side-label front">Front</div>
  <div class="side-label back">Back</div>

  <section class="page front">
    <svg viewBox="0 0 617 875" width="617" height="875">
      <defs>
        <linearGradient id="groupPhoto" x1="0" y1="0" x2="1" y2="1">
          <stop offset="0" stop-color="#e7e2d8"/>
          <stop offset=".5" stop-color="#c9a58a"/>
          <stop offset="1" stop-color="#3b5ea8"/>
        </linearGradient>
        <radialGradient id="atPhoto"><stop offset="0" stop-color="#e9e6e0"/><stop offset="1" stop-color="#b9b4aa"/></radialGradient>
        <radialGradient id="studentPhoto"><stop offset="0" stop-color="#f3ede6"/><stop offset="1" stop-color="#cfdbe6"/></radialGradient>
        <radialGradient id="chartPhoto"><stop offset="0" stop-color="#f4f4f4"/><stop offset="1" stop-color="#d6d9e0"/></radialGradient>
      </defs>
      <rect role="img" aria-label="Group of smiling students sitting on steps" x="0" y="0" width="617" height="360" fill="url(#groupPhoto)"/>
      <polygon fill="var(--yellow)" points="0,153 617,342 617,372 0,180"/>
      <polygon fill="var(--blue)" points="0,180 617,372 617,840 0,266"/>
      <polygon fill="var(--yellow)" points="0,266 617,836 617,875 590,875 0,310"/>
      <circle cx="124" cy="399" r="93" fill="var(--white)"/>
      <circle role="img" aria-label="Silver at sign on a desk" cx="124" cy="399" r="84" fill="url(#atPhoto)"/>
      <circle cx="312" cy="584" r="76" fill="var(--white)"/>
      <circle role="img" aria-label="Student giving a thumbs up at a laptop" cx="312" cy="584" r="68" fill="url(#studentPhoto)"/>
      <circle cx="489" cy="729" r="62" fill="var(--white)"/>
      <circle role="img" aria-label="Colourful 3D bar chart with a clock" cx="489" cy="729" r="55" fill="url(#chartPhoto)"/>
    </svg>

    <h2 class="abs script front-title">World Class Training</h2>
    <ul class="abs course-list">
      <li>Time Management</li>
      <li>Sales skills</li>
      <li>Strategic &amp; High performance leadership</li>
      <li>Sales Management</li>
      <li>Personal Maximum Achievement.</li>
    </ul>

    <div class="abs cost-box">
      <h3>Cost effective</h3>
      <p>Over 4 million people have completed the programs world wide, flexibility of learning &amp; the diversity of study areas</p>
    </div>
    <div class="abs phone-box">
      <svg width="16" height="16" viewBox="0 0 24 24"><path fill="var(--white)" d="M6.6 10.8a15.1 15.1 0 0 0 6.6 6.6l2.2-2.2a1 1 0 0 1 1-.25 11.4 11.4 0 0 0 3.6.57 1 1 0 0 1 1 1V20a1 1 0 0 1-1 1A17 17 0 0 1 3 4a1 1 0 0 1 1-1h3.5a1 1 0 0 1 1 1c0 1.250.2 2.45.57 3.57a1 1 0 0 1-.25 1z"/></svg>
      <span>+61 2 5550 1234</span>
    </div>

    <div class="abs brand-tile">Kelro</div>
    <div class="abs portal-name"><span class="mark"></span><span>DIGITAL HORIZON</span></div>

    <div class="abs site-box">Website:&nbsp; www.kelro-example.com.au</div>
    <div class="abs contact-box">Contact to Pay, Enrol and find out other information about the courses</div>
  </section>

  <section class="page back">
    <svg viewBox="0 0 617 875" width="617" height="875">
      <defs>
        <linearGradient id="teamPhoto" x1="0" y1="0" x2="1" y2="0">
          <stop offset="0" stop-color="#3a3f48"/>
          <stop offset=".5" stop-color="#7b7f86"/>
          <stop offset="1" stop-color="#d9dde2"/>
        </linearGradient>
        <linearGradient id="deskPhoto" x1="0" y1="0" x2="0" y2="1">
          <stop offset="0" stop-color="#2a7aa3" stop-opacity="0"/>
          <stop offset="1" stop-color="#f1ece4"/>
        </linearGradient>
      </defs>
      <rect role="img" aria-label="Business team in conversation in a bright office" x="0" y="0" width="617" height="272" fill="url(#teamPhoto)"/>
      <polygon fill="var(--yellow)" points="0,190 617,258 617,274 0,220"/>
      <polygon fill="var(--blue)" points="0,220 617,274 617,875 380,875 0,530"/>
      <polygon fill="var(--yellow)" points="0,530 380,875 350,875 0,556"/>
      <rect role="img" aria-label="Student giving a thumbs up beside a laptop and books" x="382" y="730" width="235" height="145" fill="url(#deskPhoto)"/>
    </svg>

    <h2 class="abs script back-title">Advantages of using the Kelro <span class="accent">Digital Horizon</span> Portal</h2>

    <ul class="advantages">
      <li style="left:30px;top:313px;width:500px">Cost effective, save over 50% by learning online compared to attending a Kelro class room based programme</li>
      <li style="left:30px;top:357px">learning can be scheduled around work and family</li>
      <li style="left:30px;top:386px">Reduces travel time and travel costs</li>
      <li style="left:30px;top:415px;width:540px">Students/participants have the option to select learning materials that meets their level of knowledge&nbsp; and interest.</li>
      <li style="left:30px;top:460px">Complete flexibility to build a personalised learning experience</li>
      <li style="left:30px;top:489px">Students/participants can study anywhere they have access to a computer and Internet connection</li>
      <li style="left:30px;top:518px">Self-paced learning modules allow students/participants to work at their own pace</li>
      <li style="left:52px;top:547px;width:540px">Develops knowledge of the Internet and computers skills that will help learners throughout their lives and careers</li>
      <li style="left:98px;top:587px;width:510px">Successfully completing online or computer-based courses builds self-knowledge and self-confidence and encourages students to take responsibility for their learning</li>
      <li style="left:140px;top:626px;width:470px">Join over 4 million people who have successfully undertaken the training world wide at a time &amp; a place convenient to students/participants.</li>
      <li style="left:192px;top:667px">Pay securely using swiftcoin</li>
      <li style="left:226px;top:694px;width:360px;text-align:center">Learn based on a students/participants personal financial circumstances with individual units priced at $82.50 each (this is Australian dollars &amp; includes GST)</li>
    </ul>

    <div class="abs back-brand">Kelro</div>

    <ul class="abs contact-table">
      <li><span class="val">+61 2 5550 123</span><span class="ico"><svg width="10" height="10" viewBox="0 0 24 24"><path fill="var(--white)" d="M6.6 10.8a15.1 15.1 0 0 0 6.6 6.6l2.2-2.2a1 1 0 0 1 1-.25 11.4 11.4 0 0 0 3.6.57 1 1 0 0 1 1 1V20a1 1 0 0 1-1 1A17 17 0 0 1 3 4a1 1 0 0 1 1-1h3.5a1 1 0 0 1 1 1c0 1.25.2 2.45.57 3.57a1 1 0 0 1-.25 1z"/></svg></span></li>
      <li><span class="val">alex@kelro-example.com.au</span><span class="ico"><svg width="10" height="8" viewBox="0 0 10 8"><rect x=".5" y=".5" width="9" height="7" fill="none" stroke="var(--white)"/><path d="M.5 .5 5 4.5 9.5 .5" fill="none" stroke="var(--white)"/></svg></span></li>
      <li><span class="val">www.kelro-example.com.au</span><span class="ico"><svg width="10" height="10" viewBox="0 0 10 10"><circle cx="5" cy="5" r="4.3" fill="none" stroke="var(--white)"/><path d="M.7 5h8.6M5 .7c-2.4 2.6-2.4 6 0 8.6M5 .7c2.4 2.6 2.4 6 0 8.6" fill="none" stroke="var(--white)" stroke-width=".8"/></svg></span></li>
      <li><span class="val">social.example/kelroconsulting</span><span class="ico"></span></li>
      <li><span class="val">chirp.example/alexm</span><span class="ico"></span></li>
      <li><span class="val">network.example/alexmorgan</span><span class="ico"></span></li>
    </ul>
  </section>
</body>
</html>
```